Redesign projects page on UK roofing website

Hi guys,

We would like to redesign the projects page of our roofing company website; https://www.brindlecoverings.com/projects

We would like to keep the top of the page the same (up to the big image). Also the footer design should remain the same.

We would like to have some nice photos of work we have done with a little bit of writing about each project.

This site has a nice projects page layout; https://www.tmwbuild.com/projects

Something along those lines would work well for our needs.

Thanks

```html
<!DOCTYPE html>
<html lang="en">
<head>
<meta charset="utf-8">
<title>Projects | Brindle Coverings</title>
<link href="https://fonts.googleapis.com/css2?family=Figtree:wght@400;500;600;700&display=swap" rel="stylesheet">
<style>
:root{
  --accent:#1ea9dc;
  --navy:#0c4676;
  --card-mid:#2a5d8c;
  --mist:#f2f5f8;
  --ink:#2b3440;
  --muted:#a9b6c4;
  --white:#ffffff;
}
*{box-sizing:border-box;margin:0;padding:0}
html,body{width:947px;height:1200px;overflow:hidden;background:var(--white);font-family:"Figtree",sans-serif;color:var(--ink)}
.page{position:relative;width:947px;height:1200px;overflow:hidden}
.abs{position:absolute}

/* hero */
.hero{left:0;top:0;width:947px;height:432px;background:linear-gradient(160deg,#2c2c2c 0%,#4a4a4a 40%,#5e5e5e 60%,#3a3a3a 100%)}
.hero::after{content:"";position:absolute;inset:0;background:linear-gradient(180deg,rgba(0,0,0,.45) 0%,rgba(0,0,0,.1) 30%,rgba(0,0,0,.1) 100%)}
.brand{left:182px;top:12px;display:flex;align-items:center;gap:8px;color:var(--white);font-weight:700;font-size:18px;z-index:2}
.brand-dot{width:22px;height:22px;border-radius:50%;background:var(--accent)}
.nav{left:379px;top:16px;display:flex;gap:32px;font-size:8.5px;color:var(--white);z-index:2}
.nav .current{border-bottom:1.5px solid var(--accent);padding-bottom:2px}
.btn{background:var(--accent);color:var(--white);font-weight:700;font-size:8px;display:flex;align-items:center;justify-content:center}
.hero-btn{left:677px;top:11px;width:89px;height:24px;z-index:2}
.hero-title{left:182px;top:172px;font-size:39px;font-weight:700;line-height:43px;color:var(--white);z-index:2;letter-spacing:-.5px}
.hero-title span{color:var(--accent)}
.hero-rule{left:620px;top:146px;width:1px;height:141px;background:var(--accent);z-index:2}
.hero-aside{left:634px;top:153px;width:104px;color:var(--white);z-index:2}
.hero-aside h2{font-size:17.5px;line-height:22px;font-weight:700}
.hero-aside p{font-size:9.5px;line-height:15px;margin-top:12px}

/* body */
.mist-shape{left:0;top:432px;width:947px;height:503px}
.tabs{left:184px;top:461px;display:flex;gap:10px}
.tab{height:29px;border:1px solid var(--accent);display:flex;align-items:center;padding:0 14px;gap:6px;color:var(--accent);font-weight:600;font-size:8.5px;background:var(--white)}
.tab.active{background:var(--accent);color:var(--white)}
.tab-icon{width:20px;height:20px;border-radius:50%;background:var(--accent);display:flex;align-items:center;justify-content:center}
.tab.active .tab-icon{background:var(--white)}
.section-title{left:184px;top:514px;font-size:20px;font-weight:700;color:var(--navy)}
.pager{left:596px;top:522px;display:flex;align-items:center;gap:8px;font-size:7.5px;color:var(--navy)}
.pager .muted{color:var(--muted)}
.intro{left:184px;top:551px;width:385px;font-size:7.5px;line-height:10.8px}

.card{top:619px;width:187px;height:245px;background:var(--navy);color:var(--white)}
.card-photo{width:187px;height:148px}
.card-body{padding:10px 10px}
.card h3{font-size:13px;line-height:15.5px;font-weight:700}
.card p{font-size:7.5px;line-height:10.8px;margin-top:9px}
.card.featured{background:var(--card-mid);padding:21px 10px}
.card.featured h4{font-size:7.5px;font-weight:700;margin-top:10px}
.card.featured p.desc{margin-top:1px}
.card-link{display:flex;align-items:center;gap:6px;font-size:7.5px;font-weight:700;margin-top:10px}
.dot{top:888px;width:6px;height:6px;border-radius:50%}

/* review band */
.review-band{left:2px;top:933px;width:945px;height:40px;background:var(--mist)}
.rating{left:194px;top:946px;display:flex;align-items:center;gap:8px;font-size:9px;color:#333}
.stars{display:flex;gap:2px}
.band-btn{left:675px;top:941px;width:89px;height:23px}

/* footer */
.footer{left:0;top:973px;width:947px;height:227px;background:var(--navy)}
.fcol{top:1000px;color:var(--white)}
.fcol h5{font-size:9.5px;font-weight:700;margin-bottom:9px}
.fcol ul{list-style:none;font-size:7px}
.fcol li{height:20.7px}
.social{display:flex;align-items:center;gap:6px}
.social i{width:7px;height:7px;background:var(--white);display:inline-block}
.fbrand{left:528px;top:1003px;display:flex;align-items:center;gap:8px;color:var(--white);font-weight:700;font-size:18px}
.finfo{left:528px;top:1030px;width:230px;color:var(--white);font-size:6.5px;line-height:8.5px}
.finfo p{margin-bottom:4.5px}
.badges{left:528px;top:1083px;display:flex;gap:14px;align-items:center}
.badge{background:rgba(255,255,255,.85)}
.frule{left:184px;top:1167px;width:580px;height:1px;background:rgba(255,255,255,.2)}
.copy{left:184px;top:1180px;font-size:6.5px;color:var(--white)}
</style>
</head>
<body>
<div class="page">

  <div class="abs hero" role="img" aria-label="Black and white photo of a corrugated steel roof on an industrial building"></div>
  <div class="abs brand"><span class="brand-dot"></span>brindlecoverings</div>
  <nav class="abs nav"><span>Services</span><span>Clients</span><span class="current">Projects</span><span>Team</span><span>Contact</span></nav>
  <div class="abs btn hero-btn">Get a quote</div>
  <h1 class="abs hero-title">Some of our <span>latest</span><br><span>projects.</span></h1>
  <div class="abs hero-rule"></div>
  <div class="abs hero-aside">
    <h2>What we're working on</h2>
    <p>Keep an eye on some of the latest installs, refurbs and repairs we've carried out.</p>
  </div>

  <svg class="abs mist-shape" viewBox="0 0 947 503" aria-hidden="true">
    <path d="M700 0 H947 V503 H440 C420 320 470 140 700 0 Z" fill="var(--mist)"/>
  </svg>

  <div class="abs tabs">
    <div class="tab"><span class="tab-icon"><svg width="9" height="10" viewBox="0 0 9 10"><rect x="1" y="0.5" width="7" height="9" fill="none" stroke="#fff"/><path d="M2.5 4h4M2.5 6h4" stroke="#fff"/></svg></span>All</div>
    <div class="tab active"><span class="tab-icon"><svg width="11" height="8" viewBox="0 0 11 8"><path d="M1 6 L3 1 H10 L8 6 Z" fill="none" stroke="#1ea9dc"/></svg></span>Single Ply</div>
    <div class="tab"><span class="tab-icon"><svg width="10" height="10" viewBox="0 0 10 10"><path d="M2 5 H8 L7 9 H3 Z M4 5 V2 H8" fill="none" stroke="#fff"/></svg></span>Liquid Roofing</div>
    <div class="tab"><span class="tab-icon"><svg width="11" height="8" viewBox="0 0 11 8"><path d="M1 7 L3 1 M4 7 L6 1 M7 7 L9 1 M1 7 H10" stroke="#fff" fill="none"/></svg></span>Steel Roofing</div>
    <div class="tab"><span class="tab-icon"><svg width="11" height="9" viewBox="0 0 11 9"><path d="M1 8 H10 M2 8 V4 L8 1 V8" stroke="#fff" fill="none"/></svg></span>Asphalt</div>
  </div>

  <h2 class="abs section-title">Single Ply</h2>
  <div class="abs pager">
    <svg width="17" height="6" viewBox="0 0 17 6"><path d="M17 3 H1 M4 0.5 L1 3 L4 5.5" stroke="#a9b6c4" fill="none"/></svg>
    <span class="muted">Previous Project</span>
    <span style="margin-left:9px">Next Project</span>
    <svg width="17" height="6" viewBox="0 0 17 6"><path d="M0 3 H16 M13 0.5 L16 3 L13 5.5" stroke="#0c4676" fill="none"/></svg>
  </div>
  <p class="abs intro">Single ply is one of the most popular flat roofing materials in today's market due to its lightweight and durable design. Single Ply is commonly used on large commercial buildings such as Hospitals, Schools and Universities thanks to the speed at which it can be installed. We install a variety of single ply systems including Veltra-Plan, Karro Shieldplan and Solvane Deck systems.</p>

  <article class="abs card" style="left:184px">
    <div class="card-photo" role="img" aria-label="Photo of a wet grey single ply flat roof with ductwork under a cloudy sky" style="background:linear-gradient(180deg,#8d96a0 0%,#c9ced4 35%,#4e5660 60%,#2e3640 100%)"></div>
    <div class="card-body">
      <h3>Northmoor University, Colchester</h3>
      <p>Type: Single-ply (Shieldplan)<br>Roof Size: 2300m2<br>Date of Completion: September, 2020</p>
    </div>
  </article>

  <article class="abs card featured" style="left:380px">
    <h3>Harlow Vale District Council, Uxbridge</h3>
    <p>Type: Single-ply (Veltra-Plan S)<br>Roof Size: 300m2<br>Date of Completion: March, 2020</p>
    <h4>Contract Description</h4>
    <p class="desc">The client approached Brindle to carry out a survey of their existing flat roof coverings which were leaking in numerous places. Upon inspection our engineers quickly discovered the roofs were at end of life and required replacement. Brindle replaced all of the roofs with a new Veltra-Plan single ply membrane with a 20 year manufacturer backed warranty.</p>
    <div class="card-link">Get In Touch Know More <svg width="17" height="6" viewBox="0 0 17 6"><path d="M0 3 H16 M13 0.5 L16 3 L13 5.5" stroke="#fff" fill="none"/></svg></div>
  </article>

  <article class="abs card" style="left:576px">
    <div class="card-photo" role="img" aria-label="Photo of a pale grey single ply flat roof beside houses and bare trees" style="background:linear-gradient(180deg,#9aa08f 0%,#5d6152 40%,#b7bcc2 65%,#d6dadf 100%)"></div>
    <div class="card-body">
      <h3>Private, Watford</h3>
      <p>Type: Single-ply (Veltra-Plan S)<br>Roof Size: 120m2<br>Date of Completion: February, 2020</p>
    </div>
  </article>

  <span class="abs dot" style="left:466px;background:var(--accent)"></span>
  <span class="abs dot" style="left:476px;background:#cfd6dd"></span>

  <div class="abs review-band"></div>
  <div class="abs rating">
    <span style="font-size:9.5px">Excellent</span>
    <span class="stars" aria-label="Rated 5 out of 5">
      <svg width="10" height="10" viewBox="0 0 10 10"><path d="M5 0.5 6.3 3.8 9.8 3.9 7 6 8 9.5 5 7.4 2 9.5 3 6 0.2 3.9 3.7 3.8Z" fill="#1ea9dc"/></svg>
      <svg width="10" height="10" viewBox="0 0 10 10"><path d="M5 0.5 6.3 3.8 9.8 3.9 7 6 8 9.5 5 7.4 2 9.5 3 6 0.2 3.9 3.7 3.8Z" fill="#1ea9dc"/></svg>
      <svg width="10" height="10" viewBox="0 0 10 10"><path d="M5 0.5 6.3 3.8 9.8 3.9 7 6 8 9.5 5 7.4 2 9.5 3 6 0.2 3.9 3.7 3.8Z" fill="#1ea9dc"/></svg>
      <svg width="10" height="10" viewBox="0 0 10 10"><path d="M5 0.5 6.3 3.8 9.8 3.9 7 6 8 9.5 5 7.4 2 9.5 3 6 0.2 3.9 3.7 3.8Z" fill="#1ea9dc"/></svg>
      <svg width="10" height="10" viewBox="0 0 10 10"><path d="M5 0.5 6.3 3.8 9.8 3.9 7 6 8 9.5 5 7.4 2 9.5 3 6 0.2 3.9 3.7 3.8Z" fill="#1ea9dc"/></svg>
    </span>
    <span style="font-size:7px">39 reviews on</span>
    <span style="font-size:7px;font-weight:600">ReviewStar</span>
  </div>
  <div class="abs btn band-btn">Get a quote</div>

  <footer class="abs footer"></footer>
  <div class="abs fcol" style="left:184px"><h5>Overview</h5><ul><li>Services</li><li>Clients</li><li>Projects</li><li>Team</li><li>Contact</li></ul></div>
  <div class="abs fcol" style="left:280px"><h5>Services</h5><ul><li>Asbestos roof removal</li><li>Steel cladding</li><li>Liquid waterproofing</li><li>Mastic asphalt roofing</li><li>Single ply roofing</li><li>Roof repairs</li><li>Emergency roof repairs</li></ul></div>
  <div class="abs fcol" style="left:383px"><h5>Legal</h5><ul><li>Terms of service</li></ul>
    <h5 style="margin-top:3px">Follow us</h5>
    <ul><li class="social"><i></i>Linkfolio</li><li class="social"><i></i>Snapgram</li></ul>
  </div>
  <div class="abs fbrand"><span class="brand-dot"></span>brindlecoverings</div>
  <div class="abs finfo">
    <p>Brindle Coverings Ltd is registered in England as a private limited company.</p>
    <p>Registration No: 08471529</p>
    <p>Registered Office: Unit 14 Marsh Meadow Works, Tanner Lane, Wickfield, Chelmsford CM2 9QT</p>
  </div>
  <div class="abs badges">
    <span class="badge" style="width:60px;height:22px"></span>
    <span class="badge" style="width:42px;height:26px"></span>
    <span class="badge" style="width:34px;height:34px;border-radius:50%"></span>
    <span class="badge" style="width:62px;height:24px"></span>
  </div>
  <div class="abs frule"></div>
  <p class="abs copy">© Copyright Brindle Coverings Ltd 2023 | All rights reserved.</p>

</div>
</body>
</html>
```